wealth management firm, professional group, new model

we have a logo that works but we need a card, white background using our colors...clean look

our tag line if can be used in

The Bridge From Client to Owner

```html
<!DOCTYPE html>
<html lang="en">
<head>
<meta charset="utf-8">
<title>Verra Wealth Partners – Business Card</title>
<link href="https://fonts.googleapis.com/css2?family=Poppins:wght@300;400;500;600&display=swap" rel="stylesheet">
<style>
  :root {
    --navy: #182d50;
    --navy-ink: #14223d;
    --backdrop: #bdbec0;
    --paper: #ffffff;
    --muted: #7b7d82;
    --rule: #5d6672;
  }
  * { margin: 0; padding: 0; box-sizing: border-box; }
  html, body {
    width: 1200px; height: 1000px; overflow: hidden;
    background: var(--backdrop);
    font-family: "Poppins", sans-serif;
  }
  .canvas { position: relative; width: 1200px; height: 1000px; }

  .card {
    position: absolute; left: 281px; width: 639px; height: 358px;
    border-radius: 22px;
    box-shadow: 0 4px 10px rgba(0,0,0,0.28);
  }
  .card--front { top: 70px; background: var(--navy); border: 1px solid #d7dbe2; }
  .card--back { top: 505px; background: var(--paper); border: 1px solid #e3e3e3; }

  .front-name {
    position: absolute; left: 0; right: 0; top: 162px;
    text-align: center; color: var(--paper);
    font-weight: 400; font-size: 40px; letter-spacing: 14px; padding-left: 14px;
  }

  .brand {
    position: absolute; left: 60px; width: 236px; top: 160px;
    text-align: center; color: var(--navy-ink); font-weight: 400;
  }
  .brand__name { font-size: 32px; letter-spacing: 10px; padding-left: 10px; line-height: 1; }
  .brand__sub { margin-top: 18px; font-size: 12.5px; letter-spacing: 2px; padding-left: 2px; }

  .divider {
    position: absolute; left: 319px; top: 98px; width: 2px; height: 162px;
    background: var(--rule);
  }

  .contact {
    position: absolute; left: 332px; width: 240px; top: 100px;
    text-align: center;
  }
  .contact__name { color: var(--navy); font-weight: 600; font-size: 22px; line-height: 30px; }
  .contact__title {
    color: var(--navy); font-weight: 500; font-size: 14px;
    letter-spacing: 3.5px; padding-left: 3.5px; line-height: 18px;
  }
  .contact__icons { margin-top: 18px; height: 20px; }
  .contact__lines {
    margin-top: 6px; color: var(--muted); font-weight: 300;
    font-size: 15.5px; line-height: 19.5px;
  }
</style>
</head>
<body>
<div class="canvas">
  <section class="card card--front">
    <div class="front-name">VERRA</div>
  </section>

  <section class="card card--back">
    <div class="brand">
      <div class="brand__name">VERRA</div>
      <div class="brand__sub">WEALTH PARTNERS</div>
    </div>

    <div class="divider"></div>

    <div class="contact">
      <div class="contact__name">Name Surname</div>
      <div class="contact__title">TITLE</div>
      <svg class="contact__icons" width="100" height="20" viewBox="0 0 100 20" aria-label="phone, email, website">
        <g fill="var(--navy-ink)">
          <path d="M9 4.5c-.6-.6-1.4-.5-1.9 0L5.8 5.8c-.6.7-.6 2 .5 4 1.3 2.3 3.4 4.5 5.5 5.6 1.7.9 2.9.9 3.6.3l1.3-1.3c.5-.5.5-1.3 0-1.8l-1.6-1.4c-.5-.4-1.2-.4-1.6 0l-.9.8c-1.3-.6-2.8-2.1-3.4-3.4l.8-.9c.4-.5.4-1.2 0-1.6z"/>
          <circle cx="25" cy="10" r="1.6"/>
          <rect x="34" y="4" width="20" height="13" rx="1"/>
          <circle cx="63" cy="10" r="1.6"/>
        </g>
        <path d="M35 5l9 7 9-7" stroke="#fff" stroke-width="1.6" fill="none"/>
        <g fill="none" stroke="var(--navy-ink)" stroke-width="1.5">
          <circle cx="81" cy="10" r="7.5"/>
          <ellipse cx="81" cy="10" rx="3.3" ry="7.5"/>
          <path d="M73.5 10h15M75 6h12M75 14h12M81 2.5v15"/>
        </g>
      </svg>
      <div class="contact__lines">
        <div>012 345 6789</div>
        <div>email@verrawealth.com</div>
        <div>verrawealth.com</div>
      </div>
    </div>
  </section>
</div>
</body>
</html>
```